QTM Conference promo flyers x6

We are a Registered Training Organisation and need material for an industry conference. We offer:
 Nationally Recognised Training
 Continuing Professional Education (CPE)

Tag lines - Get Qualified NOW! or Study with an RTO that understands and supports the bookkeeping industry or Our key focus is on your education and your success.
Images supplied, you can use others.

I need:
1 x DL trifold flyer front and back (all courses we offer) See DL Flyer information for a rough guide, gloss, full colour. Australian english.
1 x Vantel88 FAQ in A4 - See file
1 x QTM Conference brochure_A4 - See file
4 x Different double sided A4 flyers promoting courses we offer: Payroll, Accounting, Bookkeeping and CPE - See files KRT72806 DIPLOMA OF PAYROLL SERVICES_A4, KRT72609 DIPLOMA OF ACOUNTING_A4, CPE

Need each AI file in case a quick edit is required.

Target Market(s)

Bookkeepers

Industry/Entity Type

Bookkeeper

Font styles to use
Serif
Sans Serif

Colors

Designer to choose colors to be used in the design.

Requirements
Must have
• Branding but you can add a bit of flair
Nice to have
• I've given text but add some marketing flair.

```html
<!DOCTYPE html>
<html lang="en-AU">
<head>
<meta charset="utf-8">
<title>Vantel88 DL Tri-fold Brochure</title>
<link rel="stylesheet" href="https://fonts.googleapis.com/css2?family=Roboto:ital,wght@0,300;0,400;0,500;0,700;1,400&family=Ubuntu:wght@500;700&family=Roboto+Condensed:wght@400&display=swap">
<style>
:root{
  --stage:#8f9296;
  --ink:#111111;
  --green:#7dc242;
  --green-dark:#6cb233;
  --paper:#ffffff;
  --body:#6b6f76;
  --title:#2a2a2a;
  --grey-bar:#6d6f72;
  --photo-a:#d9dde2;
  --photo-b:#aeb5bd;
}
*{margin:0;padding:0;box-sizing:border-box}
html,body{width:1200px;height:1200px;overflow:hidden;background:var(--stage);font-family:"Roboto",sans-serif}
.spread{position:absolute;left:256px;width:687px;height:490px;background:var(--paper);overflow:hidden}
.spread--outside{top:34px}
.spread--inside{top:581px}
.spread svg.shapes{position:absolute;left:0;top:0;width:687px;height:490px}
.abs{position:absolute}

/* features panel */
.feature{position:absolute;left:30px;width:190px}
.feature__head{display:flex;align-items:center;gap:8px;font-size:9px;color:var(--title);font-weight:500}
.feature__head svg{width:14px;height:14px;flex:none}
.rule{width:14px;height:1.5px;background:var(--green);margin:6px 0 6px 22px}
.feature p{font-size:5.6px;line-height:11px;color:var(--body)}

/* CPE panel */
.cpe{left:236px;width:216px;text-align:center;color:#fff}
.cpe h2{font-size:11.5px;font-weight:700;position:absolute;top:27px;left:0;right:0}
.cpe .bar{width:16px;height:1.5px;background:var(--green);margin:0 auto}
.cpe__body{position:absolute;top:63px;left:20px;right:20px;font-size:5.4px;line-height:9.6px;color:#eee}
.cpe__ask{position:absolute;top:186px;left:0;right:0;font-size:8.4px;line-height:12px;color:var(--green);font-weight:500}
.cpe__contact{position:absolute;top:216px;left:0;right:0;font-size:11.5px;font-weight:500;letter-spacing:-.2px}
.cpe__details{position:absolute;top:249px;left:0;right:0;font-size:5.6px;line-height:11px;color:#ddd}

/* cover panel */
.cover__headline{left:478px;top:170px;font-family:"Ubuntu",sans-serif;font-weight:700;font-size:24px;line-height:28px;color:var(--green)}
.cover__visit{left:478px;top:270px;font-size:11.5px;line-height:14.5px;color:#fff;font-style:italic;font-weight:300}
.cover__list{left:478px;top:311px;width:190px;list-style:none;color:#fff;font-size:9.4px;line-height:11.6px}
.cover__list li{position:relative;padding-left:17px;margin-bottom:4.6px}
.cover__list li::before{content:"";position:absolute;left:1px;top:5px;width:4px;height:4px;border-radius:50%;background:var(--green)}
.brandname{display:flex;align-items:center;gap:6px;font-family:"Roboto",sans-serif;font-weight:300;letter-spacing:-1px}
.brandname span.mark{display:block;background:var(--green)}
.cover__brand{left:494px;top:437px;font-size:29px;color:#fff}
.cover__brand .mark{width:26px;height:26px}

/* inside: qualifications */
.inside__brand{left:32px;top:33px;font-size:29px;color:#7a7c80}
.inside__brand .mark{width:26px;height:26px}
.sec-title{font-size:9.6px;color:var(--title);font-weight:500}
.sec-body{font-size:5.7px;line-height:11px;color:var(--body)}
.checks{list-style:none;font-size:5.7px;color:var(--body)}
.checks li{position:relative;padding-left:15px;line-height:11px}
.checks li::before{content:"";position:absolute;left:1px;top:2.5px;width:4px;height:2px;border-left:1.3px solid var(--green);border-bottom:1.3px solid var(--green);transform:rotate(-45deg)}
.checks--spaced li{margin-bottom:5px}
.new{color:var(--green);font-weight:700}

/* skill sets */
.skill__icon{left:253px;top:146px;width:29px;height:29px;background:var(--green);border-radius:2px}
.skill__title{left:253px;top:188px;font-size:12px;font-weight:700;color:#fff}
.skill__body{left:253px;top:222px;width:198px;font-size:5.5px;line-height:11px;color:#eee}
.skill__list{left:253px;top:254px;width:198px;list-style:none;font-size:5.5px;line-height:7px;color:#fff}
.skill__list li{position:relative;padding-left:7px;margin-bottom:6.6px}
.skill__list li::before{content:"";position:absolute;left:1px;top:2.5px;width:2px;height:2px;border-radius:50%;background:var(--green)}

/* individual units */
.units__title{left:478px;top:23px;font-size:12.4px;font-weight:700;color:var(--green)}
.units__intro{left:481px;top:44px;width:190px;font-size:5.5px;line-height:9.6px;color:var(--body)}
.units__col{top:80px;width:94px;list-style:none;font-size:4.8px;line-height:8px;color:var(--body)}
.units__col li{position:relative;padding-left:6px;margin-bottom:3.4px}
.units__col li::before{content:"›";position:absolute;left:0;top:-1px;color:var(--green);font-size:6px}

.caption{position:absolute;top:1117px;left:0;width:1200px;text-align:center;font-family:"Roboto Condensed",sans-serif;font-size:20px;color:#f4f4f4}
</style>
</head>
<body>

<!-- OUTSIDE SPREAD -->
<section class="spread spread--outside">
  <svg class="shapes" viewBox="0 0 687 490" aria-hidden="false">
    <defs>
      <linearGradient id="photoGrey" x1="0" y1="0" x2="1" y2="1">
        <stop offset="0" stop-color="var(--photo-a)"/><stop offset="1" stop-color="var(--photo-b)"/>
      </linearGradient>
      <linearGradient id="photoWarm" x1="0" y1="0" x2="1" y2="1">
        <stop offset="0" stop-color="#e6e2dc"/><stop offset="1" stop-color="#b9b2aa"/>
      </linearGradient>
    </defs>
    <polygon points="60,0 231,0 231,190" fill="url(#photoGrey)" role="img" aria-label="Photo of a cheerful woman stretching at her office desk"/>
    <polygon points="231,0 396,0 687,250 687,490 524,490 231,218" fill="var(--ink)"/>
    <polygon points="396,0 687,0 687,250" fill="url(#photoGrey)" role="img" aria-label="Photo of smiling businesswomen in front of a celebrating team"/>
    <polygon points="231,218 231,490 524,490" fill="url(#photoWarm)" role="img" aria-label="Photo of a woman writing at a desk"/>
    <rect x="0" y="476" width="231" height="14" fill="var(--green)"/>
  </svg>

  <div class="feature" style="top:125px">
    <div class="feature__head"><svg viewBox="0 0 14 14"><polygon points="7,1 8.8,5.2 13,5.4 9.7,8.2 10.8,12.6 7,10.2 3.2,12.6 4.3,8.2 1,5.4 5.2,5.2" fill="none" stroke="var(--green)" stroke-width=".9"/></svg>Quality</div>
    <div class="rule"></div>
    <p>We are commited to delivering<br>the highest standard of education<br>and want you to succeed.</p>
  </div>
  <div class="feature" style="top:193px">
    <div class="feature__head"><svg viewBox="0 0 14 14"><circle cx="5" cy="5" r="2.5" fill="none" stroke="var(--green)" stroke-width=".9"/><path d="M1 12c0-3 2-4.5 4-4.5s4 1.5 4 4.5z" fill="none" stroke="var(--green)" stroke-width=".9"/><circle cx="10" cy="5" r="2" fill="none" stroke="var(--green)" stroke-width=".9"/></svg>Assessors</div>
    <div class="rule"></div>
    <p>Our team are a group of well qualified industry experts who<br>are experienced and committed to quality education.</p>
  </div>
  <div class="feature" style="top:252px">
    <div class="feature__head"><svg viewBox="0 0 14 14"><rect x="1" y="3" width="12" height="9" fill="none" stroke="var(--green)" stroke-width=".9"/><path d="M5 3V1.5h4V3M1 7h12" fill="none" stroke="var(--green)" stroke-width=".9"/></svg>Practical Focus</div>
    <div class="rule"></div>
    <p>Your course includes learning relevant, practical skills the can<br>be used in the workplace.</p>
  </div>
  <div class="feature" style="top:308px">
    <div class="feature__head"><svg viewBox="0 0 14 14"><rect x="1.5" y="1.5" width="11" height="11" fill="none" stroke="var(--green)" stroke-width=".9"/><path d="M5 1.5v6l1.5-1 1.5 1v-6M1.5 10h11" fill="none" stroke="var(--green)" stroke-width=".9"/></svg>Award</div>
    <div class="rule"></div>
    <p>Successfull student receive a nationally recognised<br>Qualification or Statement of Attainment.</p>
  </div>
  <div class="feature" style="top:362px">
    <div class="feature__head"><svg viewBox="0 0 14 14"><circle cx="7" cy="7" r="5.5" fill="none" stroke="var(--green)" stroke-width=".9"/><ellipse cx="7" cy="7" rx="2.4" ry="5.5" fill="none" stroke="var(--green)" stroke-width=".9"/><path d="M1.5 7h11" stroke="var(--green)" stroke-width=".9"/></svg>Convenience</div>
    <div class="rule"></div>
    <p>Study at your convienience and complete your course around<br>other life commitments.</p>
  </div>
  <div class="feature" style="top:416px">
    <div class="feature__head"><svg viewBox="0 0 14 14"><ellipse cx="7" cy="3" rx="5" ry="1.8" fill="none" stroke="var(--green)" stroke-width=".9"/><path d="M2 3v8c0 1 2.2 1.8 5 1.8s5-.8 5-1.8V3M2 7c0 1 2.2 1.8 5 1.8S12 8 12 7" fill="none" stroke="var(--green)" stroke-width=".9"/></svg>Support</div>
    <div class="rule"></div>
    <p>Assessors are practising industry experience who can advise<br>on study, career and industry opportunities.</p>
  </div>

  <div class="cpe abs" style="top:0;height:300px">
    <h2>What is CPE?</h2>
    <div class="bar" style="position:absolute;top:47px;left:100px"></div>
    <p class="cpe__body">CPE has been introduced under the Tax Agent Service regime to ensure agents registered with the TPB remain informed on current developments in the dynamic financial services industry and maintain a high level of professional knowledge and the appropriate skills to competently deliver the services they are registered to perform.<br>The Tax Practitioners Board define CPE as "any education activity relevant to the tax (financial) advice, tax agent or BAS services you provide that maintains, develops or promotes your skills, knowledge or attributes, is considered to be a continuing professional education (CPE) activity under the CPE policy."</p>
    <p class="cpe__ask">ASK our team about<br>our conference specials for CPE!</p>
    <p class="cpe__contact">CONTACT US</p>
    <p class="cpe__details">Vantel88 Pty Ltd<br>T: 1300 555 019<br>W: www.vantel88.com.au<br>E: info@vantel88.com.au</p>
  </div>

  <h1 class="abs cover__headline">education<br>is the key to<br>success</h1>
  <p class="abs cover__visit">Visit us at QTM Conference 2018<br>and ask about...</p>
  <ul class="abs cover__list">
    <li>NEW Payroll Qualifications</li>
    <li>Conference Specials</li>
    <li>CPE programs</li>
    <li>Prize Draw! Enter the competition to win our NEW Payroll Administrator Skill Set (FNSSS00012).</li>
  </ul>
  <div class="abs brandname cover__brand">Vantel88<span class="mark"></span></div>
</section>

<!-- INSIDE SPREAD -->
<section class="spread spread--inside">
  <svg class="shapes" viewBox="0 0 687 490">
    <defs>
      <linearGradient id="photoTeam" x1="0" y1="0" x2="0" y2="1">
        <stop offset="0" stop-color="#cfd3d8"/><stop offset="1" stop-color="#8e959d"/>
      </linearGradient>
    </defs>
    <polygon points="231,0 456,0 456,207 231,47" fill="url(#photoTeam)" role="img" aria-label="Photo of a business team applauding"/>
    <polygon points="231,47 456,207 456,477 231,477" fill="var(--ink)"/>
    <rect x="0" y="477" width="231" height="13" fill="var(--grey-bar)"/>
    <rect x="231" y="477" width="225" height="13" fill="var(--green)"/>
  </svg>

  <div class="abs brandname inside__brand">Vantel88<span class="mark"></span></div>
  <h3 class="abs sec-title" style="left:29px;top:68px">Qualifications</h3>
  <p class="abs sec-body" style="left:29px;top:97px;width:190px">A qualification is a certification awarded that recognises the successful completion of a nationally recognised training program. A qualification contains a selection of individual units of competency.</p>
  <ul class="abs checks checks--spaced" style="left:29px;top:153px">
    <li>Diploma of Payroll Services (KRT72806) <span class="new">NEW</span></li>
    <li>Diploma of Accounting (KRT72609)</li>
    <li>Certificate IV in Accounting and Bookkeeping (FNS40217)</li>
    <li>Diploma of Leadership and Management (BSB51915)</li>
    <li>Certificate IV in Leadership and Management (BSB42015)</li>
    <li>Certificate IV in Work Health and Safety (BSB41415)</li>
  </ul>
  <h3 class="abs sec-title" style="left:29px;top:270px">TPB Approved</h3>
  <p class="abs sec-body" style="left:29px;top:299px;width:192px">The Tax Practitioners Board (TPB) approved certain courses as meeting their specific requirements in addition to those offered under the AQF framework.<br>The units listed under this category have been been independently certified by Professor Alan Whitmore BEc LLB(Sydney) LLM(Cambridge) and formally approved by the Tax Practitioners Board and comply with the Boards specific requirements.</p>
  <ul class="abs checks" style="left:29px;top:394px;width:190px">
    <li>BAS Agent Registration Compliance Program Skill Set (FNSSS00004)</li>
    <li>TASA 2009, including the code (CPE0317)</li>
    <li>BAS and Payroll Challenge Exam (CPE05) – a fast track approach to meeting the education requirements for BAS agent registration.</li>
  </ul>

  <div class="abs skill__icon">
    <svg viewBox="0 0 29 29" width="29" height="29"><circle cx="14.5" cy="12" r="5" fill="none" stroke="#fff" stroke-width="1"/><path d="M12.5 17v3h4v-3M14.5 4v2M7 12H5M24 12h-2M9 6.5 7.8 5.3M20 6.5l1.2-1.2" stroke="#fff" stroke-width="1" fill="none"/></svg>
  </div>
  <h3 class="abs skill__title">Skill Sets</h3>
  <p class="abs skill__body">A Skill Set is a shorter program consisting of two or more units of competency. A nationally recognised Statement of Attainment is awarded on successful completion of a Skill Set.</p>
  <ul class="abs skill__list">
    <li>BAS Agent Registration Skill Set (FNSSS00004)</li>
    <li>Commercial Law for Tax Agents Skill Set (FNSSS00005)</li>
    <li>Tax Law for Tax Agents Skill Set (Tax documentation)<br>(FNSSS00008)</li>
    <li>Payroll Administrator Skill Set (FNSSS00012) NEW</li>
    <li>Business Ethics and Conduct Skill Set (FNSSS00013)</li>
    <li>Accounting Principles Skill Set (FNSSS00014)</li>
    <li>Advanced Accounting Principles Skill Set (FNSSS00015)</li>
    <li>Copyright Skill Set (BSBSS00035)</li>
    <li>Key Management Skill Set (BSBSS00043)</li>
    <li>Trade Mark Skill Set (BSBSS00057)</li>
    <li>Workforce Planning and Development Skill Set<br>(BSBSS00059)</li>
    <li>Team Leader Skill Set (BSBSS00063)</li>
    <li>Promoting Diversity Awareness in the Workplace Skill Set<br>(BSBSS00064)</li>
  </ul>

  <h3 class="abs units__title">Individual Units</h3>
  <p class="abs units__intro">Individual units are an excellent CPE activity and contribute to Qualifications and Skill Sets. A nationally recognised Statement of Attainment is awarded on successful completion of a unit.</p>
  <ul class="abs units__col" style="left:478px">
    <li>Complete business activity and instalment activity statements (FNSTPB401)</li>
    <li>Establish and maintain payroll systems (FNSTPB402)</li>
    <li>Process salary packaging arrangements and additional allowances in payroll (FNSPAY501)</li>
    <li>Process superannuation payments in payroll (FNSPAY502)<br>Process complex employee terminations in payroll (FNSPAY503)</li>
    <li>Interpret and apply knowledge of industrial regulations relevant to payroll (FNSPAY504)</li>
    <li>Interpret and apply knowledge of taxation systems relevant to payroll (FNSPAY505)</li>
    <li>Apply legal principles in contract and consumer law (FNSTPB503)</li>
    <li>Apply legal principles in corporations and trust law (FNSTPB504)</li>
    <li>Apply legal principles in property law (FNSTPB505)</li>
    <li>Apply taxation requirements when providing tax (financial) advice services (FNSTPB506)</li>
    <li>Apply legal principles in commercial law when providing tax (financial) advice services (FNSTPB507)</li>
    <li>Manage personal work priorities and professional development (BSBWOR501)</li>
    <li>Introduce cloud computing into business operations (BSBSMB412)</li>
    <li>Maintain inventory records (FNSACC405)</li>
  </ul>
  <ul class="abs units__col" style="left:580px">
    <li>Produce job costing information (FNSACC407)</li>
    <li>Work effectively in the accounting and bookkeeping industry (FNSACC408)</li>
    <li>Process business tax requirements (FNSACC411)</li>
    <li>Prepare operational budgets (FNSACC412)</li>
    <li>Prepare financial statements for non-reporting entities (FNSACC414)</li>
    <li>Establish and maintain accounting information systems (FNSACC505)</li>
    <li>Provide financial and business performance information (FNSACC511)</li>
    <li>Prepare tax documentation for individuals (FNSACC512)</li>
    <li>Manage budgets and forecasts (FNSACC513)</li>
    <li>Prepare financial reports for corporate entities (FNSACC514)</li>
    <li>Implement and maintain internal control procedures (FNSACC516)</li>
    <li>Provide management accounting information (FNSACC517)</li>
    <li>Prepare and administer tax documentation for legal entities (FNSACC601)</li>
    <li>Evaluate business performance (FNSACC607)</li>
    <li>Identify situations requiring complex ethical decision making (FNSINC503)</li>
    <li>Apply ethical frameworks and principles to make and act upon decisions (FNSINC504)</li>
  </ul>
</section>

<p class="caption">DL Size Tri-fold Brochure Design</p>
</body>
</html>
```